Business Card For Kelmora Financial Consulting

Hi, I would like a business card designed. Bold, modern.
Please use the same design as the logo. I have also attached the website design to see the overall theme.
Wordmark Font
Color: Hex: #01AEF7

```html
<!DOCTYPE html>
<html lang="en">
<head>
<meta charset="utf-8">
<title>Kelmora Consulting – Business Card</title>
<link href="https://fonts.googleapis.com/css2?family=Montserrat:wght@400;500;700;800&display=swap" rel="stylesheet">
<style>
  :root {
    --backdrop: #03aef7;
    --card-dark: #18222c;
    --card-light: #ffffff;
    --brand-blue: #01aef7;
    --text-light: #ffffff;
    --text-dark: #18222c;
  }
  * { margin: 0; padding: 0; box-sizing: border-box; }
  html, body {
    width: 1200px; height: 1200px; overflow: hidden;
    background: var(--backdrop);
    font-family: "Montserrat", Arial, sans-serif;
  }
  .canvas { position: relative; width: 1200px; height: 1200px; }

  /* Front card */
  .card-front {
    position: absolute; left: 215px; top: 94px; width: 770px; height: 440px;
    background: var(--card-light); border-radius: 28px; overflow: hidden;
  }
  .front-panel {
    position: absolute; left: 0; top: 0; width: 770px; height: 358px;
    background: var(--card-dark); border-radius: 28px;
  }
  .brand-lockup { position: absolute; display: flex; align-items: center; }
  .brand-square { border: 5px solid var(--brand-blue); flex: none; }
  .brand-name {
    color: var(--text-light); font-weight: 800; line-height: 1;
    text-transform: uppercase;
  }
  .brand-name .brand-sub { display: block; }

  .front-panel .brand-lockup { left: 131px; top: 139px; gap: 20px; }
  .front-panel .brand-square { width: 82px; height: 82px; }
  .front-panel .brand-name { font-size: 62px; letter-spacing: 1px; }
  .front-panel .brand-sub { font-size: 21px; letter-spacing: 22.5px; margin-top: 12px; }

  .website {
    position: absolute; left: 0; right: 0; top: 392px; text-align: center;
    font-size: 17px; font-weight: 700; letter-spacing: 4.2px; color: var(--text-dark);
  }

  /* Back card */
  .card-back {
    position: absolute; left: 215px; top: 636px; width: 770px; height: 440px;
    background: var(--card-dark); border-radius: 28px; overflow: hidden;
  }
  .card-back .brand-lockup { left: 81px; top: 68px; gap: 14px; }
  .card-back .brand-square { width: 55px; height: 55px; border-width: 3px; }
  .card-back .brand-name { font-size: 41px; letter-spacing: 0.5px; }
  .card-back .brand-sub { font-size: 14px; letter-spacing: 15.3px; margin-top: 8px; }

  .person-name {
    position: absolute; left: 81px; top: 173px;
    font-size: 38px; font-weight: 700; letter-spacing: 4px; color: var(--text-light);
  }
  .person-role {
    position: absolute; left: 81px; top: 217px;
    font-size: 17px; font-weight: 500; letter-spacing: 3.6px; color: var(--brand-blue);
  }
  .contact-list { position: absolute; left: 81px; top: 278px; list-style: none; }
  .contact-item {
    display: flex; align-items: center; height: 40px;
    font-size: 17px; font-weight: 400; letter-spacing: 1.6px; color: var(--text-light);
  }
  .contact-icon { width: 28px; height: 22px; margin-right: 15px; flex: none; }
</style>
</head>
<body>
<main class="canvas">

  <section class="card-front">
    <div class="front-panel">
      <div class="brand-lockup">
        <span class="brand-square"></span>
        <span class="brand-name">Kelmora<span class="brand-sub">Consulting</span></span>
      </div>
    </div>
    <p class="website">WWW.KELMORACONSULTING.COM</p>
  </section>

  <section class="card-back">
    <div class="brand-lockup">
      <span class="brand-square"></span>
      <span class="brand-name">Kelmora<span class="brand-sub">Consulting</span></span>
    </div>

    <h1 class="person-name">JOHN SMITH</h1>
    <p class="person-role">CEO &amp; FOUNDER</p>

    <ul class="contact-list">
      <li class="contact-item">
        <svg class="contact-icon" viewBox="0 0 28 22" aria-hidden="true">
          <rect x="0" y="2" width="28" height="18" rx="2" fill="#fff"/>
          <path d="M1 3 L14 12 L27 3" fill="none" stroke="#18222c" stroke-width="2.5"/>
        </svg>
        infokelmora@mailbox.com
      </li>
      <li class="contact-item">
        <svg class="contact-icon" viewBox="0 0 28 22" aria-hidden="true">
          <path d="M4 2 C2 4 1 7 4 12 C7 17 11 20 15 21 L18 18 L14 14 L11 16 C9 14 7 11 7 9 L9 6 Z" fill="#fff"/>
          <path d="M14 2 A8 8 0 0 1 22 10" fill="none" stroke="#fff" stroke-width="2"/>
          <path d="M14 6 A4 4 0 0 1 18 10" fill="none" stroke="#fff" stroke-width="2"/>
        </svg>
        +1 888 888 8888
      </li>
      <li class="contact-item">
        <svg class="contact-icon" viewBox="0 0 28 22" aria-hidden="true">
          <path d="M10 0 C4.5 0 1 4 1 8.5 C1 14 10 22 10 22 C10 22 19 14 19 8.5 C19 4 15.5 0 10 0 Z" fill="#fff"/>
          <circle cx="10" cy="8.5" r="3.5" fill="#18222c"/>
        </svg>
        321 lorem ipsum dolor
      </li>
    </ul>
  </section>

</main>
</body>
</html>
```